An international wholesale business needs letterhead design

Logo file is attached. Please design a letterhead with the following details:

- Company Name and Logo
- Address
- VAT Registration number
- Phone No
- Website address

```html
<!DOCTYPE html>
<html lang="en">
<head>
<meta charset="utf-8">
<title>Corvane Trading Letterhead</title>
<link rel="stylesheet" href="https://fonts.googleapis.com/css2?family=Inter:wght@400;600&family=Arimo:wght@400&display=swap">
<style>
  :root {
    --backdrop: #e3e4e6;
    --paper: #f1f1f2;
    --brand-red: #a41f24;
    --brand-grey: #6d7378;
    --ink: #474a4d;
    --ink-soft: #55585b;
  }
  * { box-sizing: border-box; margin: 0; padding: 0; }
  html, body { width: 1200px; height: 1141px; overflow: hidden; }
  body { background: var(--backdrop); font-family: "Arimo", Arial, sans-serif; }

  .letterhead {
    position: absolute; left: 208px; top: 20px;
    width: 784px; height: 1101px;
    background: var(--paper);
    box-shadow: 0 2px 8px rgba(0,0,0,0.12);
  }

  .brand {
    position: absolute; left: 54px; top: 86px;
    display: flex; align-items: center; gap: 8px;
    width: 216px;
  }
  .brand-dot { width: 30px; height: 30px; border-radius: 50%; background: var(--brand-red); flex: none; }
  .brand-name {
    font-family: "Inter", sans-serif; font-weight: 600; font-size: 15.5px;
    letter-spacing: 0.4px; color: var(--brand-red); white-space: nowrap;
  }

  .divider { position: absolute; top: 82px; width: 1px; height: 44px; background: var(--brand-red); }
  .divider.first { left: 299px; }
  .divider.second { left: 530px; }

  .contact, .address {
    position: absolute; top: 76px;
    font-family: "Inter", sans-serif; font-size: 13.5px; line-height: 17px; color: var(--ink);
  }
  .contact { left: 332px; }
  .address { left: 560px; font-style: normal; }
  .contact li { list-style: none; display: flex; align-items: center; gap: 9px; }
  .contact svg { width: 10px; height: 10px; fill: var(--brand-red); flex: none; }

  .letter { position: absolute; left: 59px; top: 270px; width: 667px; color: var(--ink-soft); }
  .salutation { font-size: 19px; color: var(--ink); margin-bottom: 24px; }
  .letter p.body { font-size: 11.1px; line-height: 16.8px; text-align: justify; margin-bottom: 16px; }
  .closing { font-size: 11.1px; margin-top: 33px; }
  .signature {
    width: 225px; height: 56px; margin-top: 20px;
    background: linear-gradient(90deg, rgba(40,40,40,0.12), rgba(40,40,40,0.04));
    border-radius: 4px;
  }

  .footer-band { position: absolute; left: 0; bottom: 0; height: 14px; }
  .footer-band.red { width: 512px; background: var(--brand-red); }
  .footer-band.grey { left: 516px; right: 0; background: var(--brand-grey); }
</style>
</head>
<body>
  <main class="letterhead">
    <header>
      <div class="brand">
        <span class="brand-dot"></span>
        <span class="brand-name">CORVANE TRADING</span>
      </div>
      <span class="divider first"></span>
      <ul class="contact">
        <li><svg viewBox="0 0 10 10"><path d="M2 0.5 L3.6 2.6 L2.8 3.6 Q4 6 6.4 7.2 L7.4 6.4 L9.5 8 L8.4 9.5 Q3.8 9.2 0.5 1.6 Z"/></svg>555-014-2273</li>
        <li><svg viewBox="0 0 10 10"><path d="M0.5 2 H9.5 V8.5 H0.5 Z M1 2.5 L5 5.6 L9 2.5" fill="var(--brand-red)" stroke="#f1f1f2" stroke-width="0.8"/></svg>hello@corvanetrading.com</li>
        <li><svg viewBox="0 0 10 10"><circle cx="5" cy="5" r="4.3" fill="none" stroke="var(--brand-red)" stroke-width="0.9"/><ellipse cx="5" cy="5" rx="1.9" ry="4.3" fill="none" stroke="var(--brand-red)" stroke-width="0.8"/><path d="M0.7 5 H9.3 M1.5 2.8 H8.5 M1.5 7.2 H8.5" stroke="var(--brand-red)" stroke-width="0.7"/></svg>corvanetrading.com</li>
      </ul>
      <span class="divider second"></span>
      <address class="address">
        412 Alder Court<br>
        Juneau, Alaska 99801<br>
        VAT Reg : 098765432
      </address>
    </header>

    <section class="letter">
      <p class="salutation">Dear Mr. Harlow,</p>
      <p class="body">Lorem ipsum dolor sit amet, consectetur adipiscing elit. Donec orci purus, luctus vitae dignissim eu, iaculis sed purus. Vivamus faucibus, ipsum nec aliquet viverra, leo mauris condimentum ligula, sit amet sagittis enim ligula quis arcu. Nam egestas tortor id nisi porttitor mattis. In tortor ante, ultricies in suscipit a, tempus non massa. Vivamus et auctor mi. Fusce vel massa nulla. Phasellus nec eros mauris, et scelerisque orci.</p>
      <p class="body">Donec malesuada orci vitae nulla accumsan porta a id massa. Quisque accumsan iaculis magna sit amet fringilla. Maecenas consequat, magna eget tincidunt semper, odio nibh rutrum mi, id feugiat ante nisi eu risus. Vestibulum nunc orci, rhoncus a placerat in, ultricies in mi. Cras mattis varius eros, vel fringilla nisi suscipit eget. Quisque scelerisque sagittis nulla at porttitor.</p>
      <p class="body">Sed id augue vitae urna euismod commodo aliquet a quam. Pellentesque arcu velit, cursus et malesuada ut, consequat et diam. Nullam erat sem, rhoncus id ullamcorper vitae, rhoncus et arcu. In ultricies ultricies nulla, ut rutrum nisi iaculis at. Donec eu magna a metus ornare faucibus. Fusce aliquet faucibus ultricies. Morbi semper, est id tincidunt gravida, sem arcu adipiscing lacus, ac bibendum nulla leo eu purus. Quisque nec diam sed risus consectetur a ccumsan quis quis nibh. Vestibulum id purus lorem.</p>
      <p class="body">It is a long established fact that a reader will be distracted by the readable content of a page when looking at its layout. The point of using Lorem Ipsum is that it has a more-or-less normal distribution of letters, as opposed to using 'Content here, content here', making it look like readable English. Many desktop publishing packages</p>
      <p class="body">ada ut, consequat et diam. Nullam erat sem, rhoncus id ullamcorper vitae, rhoncus et arcu. In ultricies ultricies nulla, ut rutrum nisi iaculis at. Donec eu magna a metus ornare faucibus. Fusce aliquet faucibus ultricies. Morbi semper,</p>
      <p class="closing">Sincerely,</p>
      <div class="signature" role="img" aria-label="Handwritten signature of the sender"></div>
    </section>

    <span class="footer-band red"></span>
    <span class="footer-band grey"></span>
  </main>
</body>
</html>
```